Product labels for new supplements business targeting high performing creative people

I need a label design for different supplements like Whey, BCAA, Melatonin etc. that I could customize for each use case separately.

The brand is called lanternfolk.life, and it would be the first design of the labels. We haven't sold any products yet, but the target audience is people with growth mindset, people who want to be as efficient as possible and are constantly looking to improve their lifestyle. As part of that, they are also working out, but don't know much about supplements yet. Mostly people between 20-34.

I don't have a too specific idea of the expected design, though it should be light, warm, smart and minimalist, maybe have some patterns. It should looks smart and clean (and expensive). Orange and golden might be the additional colors for white. I have attached the templates of some products that I plan to sell and also the logo of the brand.

Here's what I have used for inspiration:
Brands that I like and are somewhat similar in concept: https://www.vimqera.com/ (!!specially the way they
bring "how the product helps them" in focus, not "what the product is" & https://www.pobri.care/ &
https://www.selvoda.com/sport/ & https://en.kambelo.fr/ &
https://gridmarket.com/profiles/corawellhaldesign/designs/417586

Here's how different products look like: https://prodaxel.com/catalog

Target Market(s)

target audience is people with growth mindset, people who want to be as efficient as possible and are constantly looking to improve their lifestyle. As part of that, they are also working out, but don't know much about supplements yet. Mostly people between 20-34.

Industry/Entity Type

Supplements

Font styles to use
Sans Serif

Colors
FFC000
F8CF3A
FAE287
FDF2CF
FEFAEE
F0912C
F2A743
F7CA91
FBE8D2
FDF5EE
EE7325
F08F49
F5BC92
FAE3D3
FDF4ED

Requirements
Must have
• Clean, smart and minimalist design that can be applied for different products in different sizes, like Whey protein, BCAA, vitamins etc. available here: https://prodaxel.com/catalog
Nice to have
• Patterns, expensive look
Should not have
• Doodles, too many colors

```html
<!DOCTYPE html>
<html lang="en">
<head>
<meta charset="utf-8">
<title>lanternfolk.life — Melatonin label</title>
<link rel="stylesheet" href="https://fonts.googleapis.com/css2?family=Poppins:wght@400;500;800&display=swap">
<style>
  :root {
    --page-bg: #fbfbfc;
    --label-dark: #130c0b;
    --label-warm: #2a1e1c;
    --ink-light: #f4f0ee;
    --accent-gold: #f7a23a;
    --accent-orange: #ee7325;
    --accent-red: #e8472c;
    --chevron: #e6e6e8;
  }
  * { margin: 0; padding: 0; box-sizing: border-box; }
  html, body {
    width: 1200px;
    height: 1000px;
    overflow: hidden;
    background: var(--page-bg);
  }
  .label {
    position: absolute;
    left: 330px;
    top: 110px;
    width: 540px;
    height: 780px;
    background: linear-gradient(135deg, var(--label-warm) 0%, var(--label-dark) 45%, var(--label-dark) 70%, var(--label-warm) 100%);
    font-family: "Poppins", sans-serif;
    color: var(--ink-light);
    overflow: hidden;
  }
  .brand {
    position: absolute;
    top: 96px;
    left: 0;
    width: 100%;
    text-align: center;
  }
  .brand-dot {
    display: block;
    width: 44px;
    height: 44px;
    margin: 0 auto 22px;
    border-radius: 50%;
    background: var(--accent-orange);
  }
  .brand-name {
    font-size: 38px;
    font-weight: 500;
    letter-spacing: 0.5px;
  }
  .product-name {
    position: absolute;
    top: 300px;
    left: 0;
    width: 100%;
    text-align: center;
    font-size: 68px;
    font-weight: 800;
    letter-spacing: 3px;
    background: linear-gradient(90deg, var(--accent-gold), var(--accent-orange) 55%, var(--accent-red));
    -webkit-background-clip: text;
    background-clip: text;
    color: transparent;
  }
  .dose {
    position: absolute;
    top: 385px;
    right: 48px;
    font-size: 30px;
    font-weight: 500;
  }
  .chevron {
    position: absolute;
    left: 0;
    top: 0;
  }
  .benefits {
    position: absolute;
    top: 560px;
    left: 300px;
    font-size: 21px;
    line-height: 1.3;
    letter-spacing: 0.8px;
    transform: rotate(-3deg);
    transform-origin: left top;
  }
  .benefits sup { font-size: 11px; }
  .footer {
    position: absolute;
    bottom: 40px;
    left: 50px;
    right: 48px;
    display: flex;
    justify-content: space-between;
    font-size: 21px;
    letter-spacing: 0.6px;
  }
</style>
</head>
<body>
  <main class="label">
    <div class="brand">
      <span class="brand-dot"></span>
      <p class="brand-name">lanternfolk.life</p>
    </div>

    <h1 class="product-name">MELATONIN</h1>
    <p class="dose">1 mg</p>

    <svg class="chevron" width="540" height="780" viewBox="0 0 540 780" aria-hidden="true">
      <polygon points="203,483 490,474 248,512 261,690" fill="var(--chevron)"/>
    </svg>

    <p class="benefits">Fall asleep faster<sup>*</sup><br>Stay asleep longer<sup>*</sup></p>

    <div class="footer">
      <span class="footer-type">DIETARY SUPPLEMENT</span>
      <span class="footer-count">60 TABLETS</span>
    </div>
  </main>
</body>
</html>
```